business card for a shoe shop

we would like a business card for a family owned shoe shop.
With this information included.
Darnell's Shoe Store
Family owned since 1947

then on other side
Darnell's Shoe Store
Footwear fitting specialist
Phone: 9187 2630
218 Quarry St, Fernleigh Downs 3187
(cnr. Hartwick Rd and Quarry St)
darnellshoes218@examplemail.com
if could incorporate the purple color on card i have attached.

```html
<!DOCTYPE html>
<html lang="en">
<head>
<meta charset="utf-8">
<title>Darnell's Shoe Store – Business Card</title>
<link rel="stylesheet" href="https://fonts.googleapis.com/css2?family=Montserrat:wght@300&family=Oswald:wght@600&family=Pathway+Gothic+One&display=swap">
<style>
  :root {
    --canvas: #ffffff;
    --card-purple: #8c3dff;
    --wash-pink: #ff4dff;
    --wash-soft: #ff7bff;
    --ink: #ffffff;
    --frame: rgba(255, 255, 255, 0.75);
  }
  html, body {
    margin: 0;
    padding: 0;
    width: 1200px;
    height: 1200px;
    overflow: hidden;
    background: var(--canvas);
  }
  .card {
    position: absolute;
    left: 144px;
    width: 909px;
    height: 533px;
    display: block;
  }
  .card--front { top: 35px; }
  .card--back { top: 614px; }
  .card-base { fill: var(--card-purple); }
  .card-frame { fill: none; stroke: var(--frame); stroke-width: 3; }

  .store-name { font-family: "Oswald", sans-serif; font-weight: 600; font-size: 54px; fill: var(--ink); }
  .tagline { font-family: "Montserrat", sans-serif; font-weight: 300; font-size: 33px; letter-spacing: 1px; fill: var(--ink); }
  .address { font-family: "Pathway Gothic One", sans-serif; font-size: 54px; fill: var(--ink); }
  .email { font-family: "Pathway Gothic One", sans-serif; font-style: italic; font-size: 38px; fill: var(--ink); }
  .phone { font-family: "Oswald", sans-serif; font-weight: 600; font-size: 66px; fill: var(--ink); }

  .back-name { font-family: "Oswald", sans-serif; font-weight: 600; font-size: 60px; fill: var(--ink); }
  .back-line { font-family: "Montserrat", sans-serif; font-weight: 300; font-size: 28px; letter-spacing: 1px; fill: var(--ink); }
</style>
</head>
<body>

<svg width="0" height="0" style="position:absolute" aria-hidden="true">
  <defs>
    <radialGradient id="wash-right" cx="0.7" cy="0.55" r="0.45">
      <stop offset="0" stop-color="#ff4dff" stop-opacity="0.95"/>
      <stop offset="0.7" stop-color="#ff4dff" stop-opacity="0.6"/>
      <stop offset="1" stop-color="#ff4dff" stop-opacity="0"/>
    </radialGradient>
    <radialGradient id="wash-left" cx="0.3" cy="0.7" r="0.4">
      <stop offset="0" stop-color="#ff7bff" stop-opacity="0.85"/>
      <stop offset="1" stop-color="#ff7bff" stop-opacity="0"/>
    </radialGradient>
    <g id="card-backdrop">
      <rect class="card-base" width="909" height="533"/>
      <g role="img" aria-label="Abstract pink brushstroke artwork">
        <rect width="909" height="533" fill="url(#wash-right)"/>
        <rect width="909" height="533" fill="url(#wash-left)"/>
      </g>
      <rect class="card-frame" x="22" y="22" width="864" height="486" rx="20"/>
    </g>
  </defs>
</svg>

<svg class="card card--front" viewBox="0 0 909 533" aria-label="Business card front">
  <use href="#card-backdrop"/>
  <g text-anchor="middle">
    <text class="store-name" x="455" y="129" textLength="438" lengthAdjust="spacingAndGlyphs">Darnell's Shoe Store</text>
    <text class="tagline" x="455" y="180" textLength="452" lengthAdjust="spacingAndGlyphs">Footwear fitting specialist</text>
    <text class="address" x="455" y="247" textLength="570" lengthAdjust="spacingAndGlyphs">218 Quarry St, Fernleigh Downs 3187</text>
    <text class="address" x="455" y="324" textLength="445" lengthAdjust="spacingAndGlyphs">(cnr. Hartwick Rd and Quarry St)</text>
    <text class="email" x="455" y="378" textLength="380" lengthAdjust="spacingAndGlyphs">darnellshoes218@examplemail.com</text>
    <text class="phone" x="455" y="474" textLength="478" lengthAdjust="spacingAndGlyphs">Phone: 9187 2630</text>
  </g>
</svg>

<svg class="card card--back" viewBox="0 0 909 533" aria-label="Business card back">
  <use href="#card-backdrop"/>
  <g text-anchor="middle">
    <text class="back-name" x="455" y="268">Darnell's Shoe Store</text>
    <text class="back-line" x="455" y="322">Family owned since 1947</text>
  </g>
</svg>

</body>
</html>
```